Zielgruppe
Wir sind eine Kellerei, die Weine für den Groß-, Fach- und Online-Handel produziert.
Unsere Zielgruppe ist bei diesem Produkt eine Käuferschaft, die am Thema Genuss & Wein interessiert ist.
Titel:
Glühwein rot und weiß
Aufgabe:
Moderniesieren des Design mit Wiedererkennungsfaktor von bestehendem Produkt.
Druck Vorder- und Rückenetikett für Glühwein rot und weiß
(Unser Produkt wurde druch einen Mitbewerber kopiert und im Handel platziert [Bild Replika]. Das neue Design soll sich klar abgrenzen, aber für den Kunden einen Wiedererkennungswert haben)
Aufgabenstellung
Druck:
4c - eventuell mit Veredelung (Heißfolie gold oder Lack)
Ob 1 oder 2 getrennte Eitketten für Motiv + Lebensmittelrechtliche Angaben steht offen
Wichtig:
Platz für Pflichtangaben Wein + EAN-Code
Kapsel:
Schraubverschluss einfarbig ohne Aufdruck
Etikett:
Format für Motiv: Höhe bis 80mm Breite bis 150 mm
Flaschenform:
Bordeauxflasche dunkel (siehe altes Produkt)

```html
<!DOCTYPE html>
<html lang="de">
<head>
<meta charset="utf-8">
<title>Glühwein rot – Etikett</title>
<link rel="stylesheet" href="https://fonts.googleapis.com/css2?family=Playfair+Display:ital,wght@0,400;0,600;1,900&display=swap">
<style>
  :root {
    --backdrop: #5a5a5a;
    --label-black: #0d0d0d;
    --label-edge: #1b1b1b;
    --title-white: #f4f3ef;
    --wine-red: #c0123f;
    --line-red: #a3113a;
    --deer-cream: #eee4c4;
    --deer-gold: #c8a96a;
  }
  * { margin: 0; padding: 0; box-sizing: border-box; }
  html, body {
    width: 1200px;
    height: 790px;
    overflow: hidden;
    background: var(--backdrop);
  }
  .label {
    position: absolute;
    left: 390px;
    top: 40px;
    width: 420px;
    height: 710px;
    background: var(--label-black);
    border: 1px solid var(--label-edge);
    overflow: hidden;
    font-family: "Playfair Display", Georgia, serif;
  }
  .brand {
    position: absolute;
    top: 64px;
    left: 0;
    width: 100%;
    display: flex;
    justify-content: center;
    align-items: center;
    gap: 8px;
    color: var(--title-white);
    font-weight: 400;
    font-size: 22px;
    letter-spacing: 1px;
  }
  .brand-dot {
    width: 14px;
    height: 14px;
    border-radius: 50%;
    background: var(--title-white);
  }
  .title {
    position: absolute;
    color: var(--title-white);
    font-weight: 900;
    font-style: italic;
    font-size: 190px;
    line-height: 1;
    letter-spacing: -6px;
    white-space: nowrap;
  }
  .title-gluh { left: -6px; top: 150px; }
  .title-wein { left: 82px; top: 290px; }
  .artwork {
    position: absolute;
    inset: 0;
    width: 100%;
    height: 100%;
  }
  .variety {
    position: absolute;
    left: 218px;
    top: 452px;
    color: var(--wine-red);
    font-weight: 900;
    font-style: italic;
    font-size: 36px;
    letter-spacing: 1px;
  }
</style>
</head>
<body>
  <main class="label">
    <div class="brand"><span class="brand-name">KELSGARD</span><span class="brand-dot"></span></div>

    <div class="title title-gluh">glüh</div>
    <div class="title title-wein">wein</div>

    <svg class="artwork" viewBox="0 0 420 710" xmlns="http://www.w3.org/2000/svg">
      <line x1="0" y1="477" x2="420" y2="597" stroke="var(--line-red)" stroke-width="2"/>
      <line x1="0" y1="615" x2="420" y2="465" stroke="var(--line-red)" stroke-width="2"/>
      <rect class="deer deer-leaping" role="img" aria-label="Cremefarbene Hirsch-Silhouette im Sprung" x="0" y="428" width="128" height="98" rx="6" fill="var(--deer-cream)"/>
      <rect class="deer deer-rearing" role="img" aria-label="Goldene Hirsch-Silhouette, aufsteigend" x="195" y="488" width="128" height="202" rx="6" fill="var(--deer-gold)"/>
    </svg>

    <div class="variety">rot</div>
  </main>
</body>
</html>
```